Broschüren-Design für Verkauf von Produkten aus Holz
Die Kommunikation mit dem Designer TAP war durchweg einwandfrei! Änderungswünsche wurden in kürzester Zeit umgesetzt. Jederzeit gerne wieder!
Zielgruppe
Seit über 60 Jahren fertigt die Brenzel GmbH & Co. KG Produkte aus Holz.
Zielgruppe sind Küchenstudios .
Aufgabenstellung
Brenzel-Küchenstudio Broschüre/Katalog
Aufgabenstellung:
Es soll ein Katalog (PDF zum Blättern & Druckversion) erstellt werden in 3 Sprachen speziell für Küchenstudios, aufgeteilt in 6 Rubriken (je Rubrik 2-6 Seiten) + ansprechendes Deckblatt mit unserem Logo und einem Slogan aus dem sinngemäß hervorgeht, dass es sich bei unseren Produkten um maßangefertigte Unikate aus der Natur handelt. Relativ wenig Text Gesamtumfang ca. 24-30 Seiten.
Rubriken:
- Holzarten kgz + durchgehend
- Thekenplatte & Thekenaufsätze
- Küchenarbeitsplatten
- Massivholzfronten
- Tische/Tischplatten
- Schneidbretter/Hackklotz
- Magnetmesserblöcke
Ziel:
Es soll vermittelt werden:
- Massivholz passt nahezu zu jeder Küche
- In Küchen Akzente mit Massivholzkomponenten zu setzen und diese damit aufzuwerten.
- Auf Wunschmaß individuell in Deutschland gefertigt
- Erweiterungen & Austausch auf vorhandenen Küchen möglich
Unsere Grobvorstellung:
1. Innenseite: Wir über uns... mit Bildern der Ansprechpartner sowie Luftbild Firma
2. Seite: Inhaltsverzeichnis mit Seitenzahl der erhältlichen Produkte (Rubriken)
Ab Seite 3: Bilder der einzelnen Rubriken mit KLEINEN Textfelder, diese werden nachträglich von uns bearbeitet/erstellt
Letzte Seite: Informationen über Lieferung & Lieferzeiten
Rückseite: Basierend auf Deckblatt und unserem Logo (nicht all zu groß) mit Adress & Kontaktdaten
Die Bilder für die einzelnen Rubriken werden von uns gestellt, ergänzend sollen passende Bilder aus verschiedenen Quellen zu den verschiedenen Rubriken hinzugezogen werden, die mit entsprechender Genehmigung verwendet werden dürfen.
Ansonsten steht der Gestaltung und dem Design keine weiteren Vorgaben im Weg.

```html
<!DOCTYPE html>
<html lang="de">
<head>
<meta charset="utf-8">
<title>Brenzel Küchenstudio Katalog – Präsentation</title>
<link href="https://fonts.googleapis.com/css2?family=Josefin+Sans:wght@300;400;600&family=Roboto+Condensed:wght@400&display=swap" rel="stylesheet">
<style>
:root{
  --board:#222d33;
  --paper:#ffffff;
  --navy:#2c4a82;
  --navy-deep:#1d2a4e;
  --rust:#b3451f;
  --text:#3a4a7a;
  --grey:#6b6b6b;
  --c01:#8a3e1f;
  --c02:#b5c43a;
  --c03:#1e6a7e;
  --c04:#7a3a4a;
  --c05:#b8923a;
  --c06:#b5402c;
  --c07:#1e6f8a;
}
*{margin:0;padding:0;box-sizing:border-box}
html,body{width:848px;height:1200px;overflow:hidden;background:var(--board)}
body{position:relative;font-family:"Josefin Sans",sans-serif;color:var(--text)}
.abs{position:absolute}
.spread{position:absolute;background:var(--paper);overflow:hidden;box-shadow:0 2px 6px rgba(0,0,0,.35)}
.photo{position:absolute}
.board-label{position:absolute;top:285px;font-family:"Roboto Condensed",sans-serif;font-size:13px;color:#fff;transform:translateX(-50%)}
.brand{font-family:"Josefin Sans",sans-serif;font-weight:600;color:var(--navy);letter-spacing:.3px}
.brand-dot{display:inline-block;width:5px;height:5px;border-radius:50%;background:var(--rust);margin-right:3px;vertical-align:middle}

/* cover */
.quote{position:absolute;left:40px;width:244px;top:52px;text-align:center;font-weight:400;font-size:11.5px;line-height:17px;color:var(--navy);letter-spacing:.1px}
.quote-sub{position:absolute;left:40px;width:244px;top:93px;text-align:center;font-weight:300;font-size:7.5px;color:var(--navy)}
.cover-rule{position:absolute;left:16px;top:175px;width:598px;height:5px;background:var(--rust)}
.address{position:absolute;top:192px;font-size:4.6px;line-height:6.2px;font-weight:300;color:var(--navy)}
.address b{font-weight:600}
.cover-band{position:absolute;left:325px;top:181px;width:326px;height:49px;background:linear-gradient(90deg,var(--navy-deep),var(--navy));color:#fff;text-align:center}
.cover-band .kicker{margin-top:10px;font-size:7.5px;font-weight:300}
.cover-band .claim{margin-top:7px;font-size:11.5px;font-weight:400;letter-spacing:.4px}

/* toc */
.tab{position:absolute;color:#fff;font-weight:300}
.toc-row{position:absolute;height:8px;display:flex;align-items:center;font-size:4.4px;color:#333}
.toc-num{height:7px;display:flex;align-items:center;justify-content:flex-end;padding-right:2px;color:#fff;font-size:4.4px}
.toc-label{padding-left:2px;white-space:nowrap}
.toc-dots{flex:1;border-bottom:.6px dotted #777;margin:0 2px 1px}

/* body text */
.copy{position:absolute;font-size:3.3px;line-height:4.2px;font-weight:300;color:#444;text-align:justify}
.copy p+p{margin-top:4px}
.drop{float:left;font-size:11px;line-height:9px;margin:0 1px 0 0;font-weight:300}
.person{position:absolute;font-size:6px;font-weight:400;color:var(--navy)}
.portrait{position:absolute;background:#d9d9d9}
.label-box{position:absolute;color:#fff;font-weight:300;text-align:center;overflow:hidden}
.label-box .big{position:absolute;left:0;right:0;font-size:36px;font-weight:300;opacity:.25;line-height:1}
.label-box .name{position:relative;font-size:8px;line-height:10px}
.pageno{position:absolute;font-size:3px;color:#666}
</style>
</head>
<body>

<section class="spread" style="left:99px;top:41px;width:651px;height:230px" aria-label="Rückseite und Titel">
  <div class="quote">„DETAILS SIND DER SCHLÜSSEL<br>ZUR PERFEKTION.“</div>
  <div class="quote-sub">… und deshalb kümmern wir uns um Ihre Details!</div>
  <div class="abs brand" style="left:19px;top:156px;font-size:11px"><span class="brand-dot"></span>Brenzel</div>
  <div class="photo" style="left:325px;top:0;width:326px;height:181px;background:linear-gradient(160deg,#8e8e8c 0%,#b9b5ad 35%,#c89a62 60%,#8ea2b4 100%)" role="img" aria-label="Moderne Küche mit massivem Hirnholz-Arbeitsblock, Kräutern und Korb"></div>
  <div class="abs brand" style="left:555px;top:22px;font-size:20px"><span class="brand-dot"></span>Brenzel</div>
  <div class="cover-band">
    <div class="kicker">– Küche so nachhaltig wie individuell –</div>
    <div class="claim">MASSANGEFERTIGTE UNIKATE AUS DER NATUR</div>
  </div>
  <div class="cover-rule"></div>
  <div class="address" style="left:16px"><b>Brenzel GmbH &amp; Co. KG</b><br>Mühlenweg 12<br>79312 Holzbach<br>Deutschland</div>
  <div class="address" style="left:94px;top:198px">Telefon: 07641-55210<br>Mail: info@brenzel-holz.de<br>www.brenzel-holz.de</div>
</section>
<div class="board-label" style="left:238px">Rückseite</div>
<div class="board-label" style="left:617px">Titel</div>

<section class="spread" style="left:99px;top:338px;width:490px;height:172px;z-index:1" aria-label="Inhalt">
  <div class="photo" style="left:75px;top:0;width:346px;height:94px;background:linear-gradient(180deg,#1e1f22 0%,#2c2b2a 55%,#8a5a2a 75%,#1a1a1a 100%)" role="img" aria-label="Massivholztisch mit braunen Lederstühlen vor dunkler Wand"></div>
  <div class="tab" style="left:11px;top:0;width:71px;height:102px;background:var(--navy)"><span style="position:absolute;left:10px;bottom:7px;font-size:11px">Inhalt</span></div>
  <div class="toc-row" style="left:11px;top:115px;width:160px"><span class="toc-label" style="font-weight:600">Über uns</span><span class="toc-dots"></span>x</div>
  <div class="toc-row" style="left:0;top:128px;width:172px"><span class="toc-num" style="width:19px;background:var(--c01)">01</span><span class="toc-label">Holzarten kgz + durchgehend</span><span class="toc-dots"></span>x</div>
  <div class="toc-row" style="left:0;top:137px;width:172px"><span class="toc-num" style="width:19px;background:var(--c02)">02</span><span class="toc-label">Thekenplatte &amp; Thekenaufsätze</span><span class="toc-dots"></span>x</div>
  <div class="toc-row" style="left:0;top:146px;width:172px"><span class="toc-num" style="width:19px;background:#1e6a5a">03</span><span class="toc-label">Küchenarbeitsplatten</span><span class="toc-dots"></span>x</div>
  <div class="toc-row" style="left:244px;top:120px;width:178px"><span class="toc-num" style="width:23px;background:var(--c04)">04</span><span class="toc-label">Massivholzfronten</span><span class="toc-dots"></span>x</div>
  <div class="toc-row" style="left:244px;top:129px;width:178px"><span class="toc-num" style="width:23px;background:var(--c05)">05</span><span class="toc-label">Tische/Tischplatten</span><span class="toc-dots"></span>x</div>
  <div class="toc-row" style="left:244px;top:138px;width:178px"><span class="toc-num" style="width:23px;background:var(--c06)">06</span><span class="toc-label">Schneidbretter/Hackklotz</span><span class="toc-dots"></span>x</div>
  <div class="toc-row" style="left:244px;top:147px;width:178px"><span class="toc-num" style="width:23px;background:var(--c07)">07</span><span class="toc-label">Magnetmesserblöcke</span><span class="toc-dots"></span>x</div>
</section>

<section class="spread" style="left:259px;top:504px;width:491px;height:174px;z-index:2" aria-label="Über uns">
  <div class="photo" style="left:0;top:16px;width:278px;height:158px;background:linear-gradient(135deg,#4f7a3a 0%,#8aa57a 35%,#c7cdd2 55%,#9aa0a6 70%,#5e8a45 100%)" role="img" aria-label="Luftbild des Firmengeländes mit Hallen und Solardächern"></div>
  <div class="tab" style="left:38px;top:0;width:62px;height:54px;background:var(--navy);opacity:.92"><span style="position:absolute;left:8px;bottom:7px;font-size:11px">Über uns</span></div>
  <div class="abs brand" style="left:334px;top:23px;font-size:10px"><span class="brand-dot"></span>Brenzel</div>
  <div class="person" style="left:290px;top:50px">Max Mustermann</div>
  <div class="copy" style="left:290px;top:59px;width:63px">Seit vielen Jahren begleitet er Küchenstudios bei Planung und Auswahl der passenden Hölzer.</div>
  <div class="copy" style="left:357px;top:59px;width:63px">Er berät zu Maßen, Oberflächen und Lieferzeiten und findet für jedes Projekt eine Lösung.</div>
  <div class="person" style="left:290px;top:117px">Julia Musterfrau</div>
  <div class="copy" style="left:290px;top:126px;width:63px">Sie betreut Anfragen aus dem Handel und stimmt Sonderwünsche direkt mit der Fertigung ab.</div>
  <div class="copy" style="left:357px;top:126px;width:63px">Ihr Anliegen ist eine schnelle Antwort und eine Arbeitsplatte, die genau passt.</div>
  <div class="portrait" style="left:431px;top:23px;width:48px;height:61px" role="img" aria-label="Platzhalter Foto Ansprechpartner"></div>
  <div class="portrait" style="left:431px;top:92px;width:48px;height:61px" role="img" aria-label="Platzhalter Foto Ansprechpartnerin"></div>
</section>

<section class="spread" style="left:264px;top:826px;width:486px;height:172px;z-index:3" aria-label="Küchenarbeitsplatten">
  <div class="photo" style="left:0;top:16px;width:141px;height:67px;background:linear-gradient(180deg,#d8d6d2 0%,#b98a55 60%,#5a5a5a 100%)" role="img" aria-label="Küchenzeile mit Holzarbeitsplatte und Ablagen"></div>
  <div class="photo" style="left:11px;top:92px;width:60px;height:59px;background:linear-gradient(160deg,#b98a55,#8a5f35 60%,#cfcfcf)" role="img" aria-label="Spüle in Holzarbeitsplatte"></div>
  <div class="photo" style="left:82px;top:92px;width:59px;height:59px;background:linear-gradient(160deg,#a77a48,#c79a63 50%,#e6e6e6)" role="img" aria-label="Edelstahlbecken in Eichenplatte"></div>
  <div class="abs" style="left:160px;top:0;width:74px;height:114px;background:var(--c03)"></div>
  <div class="copy" style="left:166px;top:47px;width:60px;color:#fff"><p><span class="drop" style="color:#fff">R</span>obuste Arbeitsplatten aus Eiche, Buche oder Nussbaum, keilgezinkt oder durchgehend. Jede Platte wird nach Ihren Maßen zugeschnitten und mit Ausschnitten für Spüle und Kochfeld geliefert.</p><p>Gerne beraten wir Sie zur Pflege.</p></div>
  <div class="photo" style="left:259px;top:0;width:227px;height:153px;background:linear-gradient(180deg,#cfd2d4 0%,#a97a48 40%,#b58656 62%,#eeeeee 75%,#d9d9d9 100%)" role="img" aria-label="Küche mit Eichen-Arbeitsplatte, Holz-Rückwand und weißen Fronten"></div>
  <div class="label-box" style="left:405px;top:119px;width:69px;height:53px;background:var(--c03)"><div class="name" style="top:7px">Küchenarbeits-<br>platten</div><div class="big" style="top:24px">03</div></div>
</section>

<section class="spread" style="left:99px;top:667px;width:485px;height:172px;z-index:4" aria-label="Thekenplatten und Thekenaufsätze">
  <div class="copy" style="left:11px;top:33px;width:59px"><p><span class="drop" style="color:var(--c02)">D</span>icke Thekenplatten aus Massivholz setzen in jeder Küche einen warmen Akzent. Wir fertigen sie auf Wunschmaß, passend zu vorhandenen Fronten und Arbeitsflächen. Auch ein Austausch auf bestehenden Küchen ist möglich.</p><p>Fragen Sie uns nach Holzarten und Oberflächen.</p></div>
  <div class="photo" style="left:82px;top:0;width:268px;height:145px;background:linear-gradient(150deg,#4a4a48 0%,#7a7672 35%,#c9a06a 55%,#d8d8d8 75%,#3a3a3a 100%)" role="img" aria-label="Küche mit massiver Thekenplatte aus Eiche und Barhocker"></div>
  <div class="photo" style="left:396px;top:16px;width:77px;height:48px;background:linear-gradient(180deg,#ece6e0,#8a4f2e 70%,#5a3520)" role="img" aria-label="Wandaufsatz aus Nussbaum mit Utensilien"></div>
  <div class="photo" style="left:353px;top:49px;width:74px;height:110px;border:2px solid #fff;background:linear-gradient(170deg,#dcdcdc 0%,#9aa3a0 35%,#6a4027 65%,#ececec 100%)" role="img" aria-label="Thekenaufsatz mit Messerblock und Kochfeld"></div>
  <div class="copy" style="left:433px;top:72px;width:40px"><p><span class="drop" style="color:var(--c02)">W</span>andaufsätze und Ablagen ergänzen die Theke und schaffen Platz für Gewürze und Geräte.</p><p>Jedes Teil wird in Deutschland gefertigt.</p></div>
  <div class="label-box" style="left:156px;top:119px;width:69px;height:53px;background:var(--c02)"><div class="name" style="top:5px">Thekenplatten/<br>Thekenaufsätze</div><div class="big" style="top:24px">02</div></div>
  <div class="pageno" style="left:12px;top:149px">8</div>
  <div class="pageno" style="left:472px;top:149px">9</div>
</section>

<section class="spread" style="left:99px;top:989px;width:485px;height:172px;z-index:5" aria-label="Tische und Tischplatten">
  <div class="photo" style="left:0;top:16px;width:318px;height:156px;background:linear-gradient(160deg,#5a4a3a 0%,#8a7560 30%,#c9a06a 55%,#8c9399 75%,#6a6a6a 100%)" role="img" aria-label="Esstisch aus Eiche mit grauen Samtstühlen vor Natursteinwand"></div>
  <div class="label-box" style="left:16px;top:0;width:63px;height:53px;background:var(--c05);opacity:.9"><div class="big" style="top:-2px">05</div><div class="name" style="top:30px">Tische/<br>Tischplatten</div></div>
  <div class="photo" style="left:301px;top:74px;width:102px;height:76px;border:2px solid #fff;background:linear-gradient(170deg,#3a3a3a 0%,#6a6a6a 40%,#b58656 65%,#d9d9d9 100%)" role="img" aria-label="Holztisch mit schwarzen Stühlen in dunklem Raum"></div>
  <div class="copy" style="left:331px;top:32px;width:69px"><p><span class="drop" style="color:var(--c05)">S</span>olide Tischplatten mit Baumkante oder gerader Kante, in Länge und Breite frei wählbar. Passende Gestelle aus Stahl oder Holz runden das Bild ab.</p></div>
  <div class="copy" style="left:404px;top:32px;width:69px"><p>Jeder Tisch ist ein Unikat mit eigener Maserung.</p><p>Fragen Sie nach Mustern.</p></div>
  <div class="pageno" style="left:472px;top:150px">7</div>
</section>

</body>
</html>
```